Brenwick Realty
Business cards and stationery
Brenwick Realty - Real Estate
Creative Brief
Modern
Marian Talcott
Director
Level 4 218 Garnet Lane Melbourne VIC 3000
marian@brenwickrealty-example.com.au
www.brenwickrealty-example.com.au
Brenwick Summit Realty 518902K Licensee Marian Talcott
Stationery needs to have the licensee info on the bottom of letterhead
black background logo in centre

```html
<!DOCTYPE html>
<html lang="en">
<head>
<meta charset="utf-8">
<title>Brenwick Realty – Business Cards</title>
<link rel="stylesheet" href="https://fonts.googleapis.com/css2?family=Open+Sans:wght@400;600;700&display=swap">
<style>
  :root {
    --backdrop: #ece8e2;
    --card: #121212;
    --pink: #e6177e;
    --blue: #27b5e6;
    --text: #e9e9e9;
    --muted: #9a9a9a;
    --divider: #5a5a5a;
  }
  * { box-sizing: border-box; margin: 0; padding: 0; }
  html, body {
    width: 1200px; height: 852px; overflow: hidden;
    background: var(--backdrop);
    font-family: "Open Sans", Arial, sans-serif;
  }
  .canvas { position: relative; width: 1200px; height: 852px; }
  .card {
    position: absolute;
    width: 600px; height: 366px;
    background: var(--card);
    border-radius: 22px;
    box-shadow: 0 10px 28px rgba(0,0,0,.22);
    color: var(--text);
    overflow: hidden;
  }
  .card--side { left: 70px; top: 50px; }
  .card--stacked { left: 530px; top: 436px; }

  .brand-name {
    position: absolute;
    font-weight: 700; font-size: 28px; line-height: 1.05;
    color: var(--pink);
    text-align: center;
    white-space: nowrap;
    letter-spacing: .3px;
  }
  .card--side .brand-name { left: 20px; top: 150px; width: 250px; }
  .card--stacked .brand-name { left: 170px; top: 70px; width: 260px; }
  .brand-dot {
    display: block; width: 14px; height: 14px; border-radius: 50%;
    background: var(--blue); margin: 0 auto 10px;
  }

  .divider {
    position: absolute; left: 285px; top: 52px;
    width: 1px; height: 262px; background: var(--divider);
  }

  .person-name { color: var(--pink); font-weight: 700; font-size: 20px; line-height: 1.2; white-space: nowrap; }
  .person-role { font-size: 14px; margin-bottom: 18px; }
  .card--side .person-role { color: var(--muted); }
  .card--stacked .person-role { color: var(--blue); margin-bottom: 14px; }
  .address { font-size: 14px; line-height: 1.5; color: var(--text); white-space: nowrap; }

  .card--side .details { position: absolute; left: 308px; top: 58px; }
  .card--side .address { margin-bottom: 20px; }

  .card--stacked .details { position: absolute; left: 42px; top: 210px; }
  .card--stacked .contacts { position: absolute; left: 296px; top: 212px; }

  .contacts { list-style: none; font-size: 12.5px; line-height: 1; }
  .contacts li { display: flex; align-items: center; gap: 9px; height: 22px; white-space: nowrap; }
  .contacts svg { width: 13px; height: 13px; flex: none; fill: var(--pink); }
</style>
</head>
<body>
<div class="canvas">

  <section class="card card--side" aria-label="Business card, side layout">
    <div class="brand-name"><span class="brand-dot"></span>Brenwick Realty</div>
    <div class="divider"></div>
    <div class="details">
      <p class="person-name">Marian Talcott</p>
      <p class="person-role">Director</p>
      <p class="address">Level 4<br>218 Garnet Lane<br>Melbourne VIC 3000</p>
      <ul class="contacts">
        <li><svg viewBox="0 0 16 16"><path d="M3 1l3 3-1.5 2a9 9 0 0 0 5.5 5.5L12 10l3 3-2 2C7 15 1 9 1 3z"/></svg>03 9555 0142</li>
        <li><svg viewBox="0 0 16 16"><path d="M4 0h8v16H4zM6 2v10h4V2zM7 13h2v1H7z"/></svg>0491 570 156</li>
        <li><svg viewBox="0 0 16 16"><path d="M4 1h7v4H4zM1 6h14v8H1zM4 10h8v3H4z"/></svg>03 9555 0187</li>
        <li><svg viewBox="0 0 16 16"><path d="M1 3h14v10H1zM2 4l6 5 6-5v1L8 10 2 5z" fill-rule="evenodd"/></svg>marian@brenwickrealty-example.com.au</li>
      </ul>
    </div>
  </section>

  <section class="card card--stacked" aria-label="Business card, stacked layout">
    <div class="brand-name"><span class="brand-dot"></span>Brenwick Realty</div>
    <div class="details">
      <p class="person-name">Marian Talcott</p>
      <p class="person-role">Director</p>
      <p class="address">Level 4<br>218 Garnet Lane<br>Melbourne VIC 3000</p>
    </div>
    <ul class="contacts">
      <li><svg viewBox="0 0 16 16"><path d="M3 1l3 3-1.5 2a9 9 0 0 0 5.5 5.5L12 10l3 3-2 2C7 15 1 9 1 3z"/></svg>03 9555 0142</li>
      <li><svg viewBox="0 0 16 16"><path d="M4 0h8v16H4zM6 2v10h4V2zM7 13h2v1H7z"/></svg>0491 570 156</li>
      <li><svg viewBox="0 0 16 16"><path d="M4 1h7v4H4zM1 6h14v8H1zM4 10h8v3H4z"/></svg>03 9555 0187</li>
      <li><svg viewBox="0 0 16 16"><path d="M1 3h14v10H1zM2 4l6 5 6-5v1L8 10 2 5z" fill-rule="evenodd"/></svg>marian@brenwickrealty-example.com.au</li>
      <li><svg viewBox="0 0 16 16"><path d="M8 0a8 8 0 1 0 0 16A8 8 0 0 0 8 0zm0 2a6 6 0 0 1 0 12A6 6 0 0 1 8 2zM7 2.5C5 5 5 11 7 13.5h2C11 11 11 5 9 2.5zM2 7h12v2H2z"/></svg>www.brenwickrealty-example.com.au</li>
    </ul>
  </section>

</div>
</body>
</html>
```